Commercial Construction Interior Fitout company needs Logo and Business Cards

We need a logo and business card design. We specialise in Commercial Ceilings, Partitions, Plastering and Carpentry.

Company name: 7QX Commercial Interiors. Would like a professional looking card more than a fancy look. Gloss front preferably black pattern with Fluro Green and white text.

Will need:

Name
Position
Phone
Fax
Email
Postal Address
Web address
Updates

Thank you so much everyone for your efforts and fantastic designs..   If I didn't respond to everyone personally,  my apologises. 

Again, thanks all

R.M                               

Target Market(s)

Existing & New clients in the Construction Industry

Industry/Entity Type

Business

Requirements
Nice to have
• 7QX to be overlapped or made into some sort of Logo

```html
<!DOCTYPE html>
<html lang="en">
<head>
<meta charset="utf-8">
<title>7QX Commercial Interiors – Business Cards</title>
<link rel="stylesheet" href="https://fonts.googleapis.com/css2?family=Tenor+Sans&family=Cabin:wght@400;500&display=swap">
<style>
  :root {
    --page: #ffffff;
    --card-black: #0a0a0a;
    --panel-black: #050505;
    --pattern-dark: #141414;
    --pattern-light: #2a2a2a;
    --fluro-green: #76c442;
    --accent-orange: #e9502c;
    --ink-dark: #1b2a10;
    --text-white: #f2f2f2;
    --text-grey: #cfcfcf;
  }
  * { box-sizing: border-box; margin: 0; padding: 0; }
  html, body {
    width: 1200px;
    height: 873px;
    overflow: hidden;
    background: var(--page);
  }
  .sheet {
    position: relative;
    width: 1200px;
    height: 873px;
    display: flex;
    align-items: center;
    justify-content: center;
    gap: 40px;
  }
  .card {
    position: relative;
    width: 540px;
    height: 328px;
    background: var(--card-black);
    overflow: hidden;
    box-shadow: 0 2px 10px rgba(0,0,0,0.25);
  }
  .card__pattern {
    position: absolute;
    inset: 0;
    background:
      radial-gradient(ellipse at 60% 70%, var(--pattern-light) 0%, var(--pattern-dark) 55%, var(--card-black) 100%);
  }

  /* Front */
  .front__logo {
    position: absolute;
    left: 0; right: 0;
    top: 78px;
    display: flex;
    align-items: center;
    justify-content: center;
    gap: 10px;
  }
  .logo__name {
    font-family: "Tenor Sans", sans-serif;
    font-size: 46px;
    color: var(--fluro-green);
    letter-spacing: 2px;
    line-height: 1;
  }
  .logo__mark {
    width: 16px;
    height: 16px;
    background: var(--accent-orange);
  }
  .front__band {
    position: absolute;
    left: 28px;
    right: 28px;
    top: 160px;
    height: 40px;
    border-radius: 20px;
    background: var(--fluro-green);
    display: flex;
    align-items: center;
    justify-content: center;
    font-family: "Tenor Sans", sans-serif;
    font-size: 17px;
    color: var(--ink-dark);
  }

  /* Back */
  .back__panel {
    position: absolute;
    left: 0; top: 0; bottom: 0;
    width: 300px;
    background: var(--panel-black);
  }
  .back__logo {
    position: absolute;
    left: 28px;
    top: 26px;
    display: flex;
    align-items: center;
    gap: 8px;
  }
  .back__logo .logo__name {
    font-size: 20px;
    color: var(--text-white);
    letter-spacing: 0.5px;
  }
  .back__logo .logo__mark {
    width: 10px;
    height: 10px;
  }
  .contact {
    position: absolute;
    left: 40px;
    top: 68px;
    font-family: "Cabin", sans-serif;
    color: var(--text-grey);
  }
  .contact__name {
    font-size: 20px;
    color: var(--fluro-green);
    line-height: 1.1;
  }
  .contact__position {
    font-size: 12px;
    color: var(--fluro-green);
    margin-bottom: 6px;
  }
  .contact__line {
    font-size: 13px;
    letter-spacing: 1.5px;
    line-height: 1.35;
  }
  .back__band {
    position: absolute;
    left: 0;
    right: 150px;
    bottom: 56px;
    height: 40px;
    border-radius: 0 20px 20px 0;
    background: var(--fluro-green);
    display: flex;
    align-items: center;
    justify-content: center;
    font-family: "Cabin", sans-serif;
    font-size: 15px;
    color: var(--ink-dark);
  }
</style>
</head>
<body>
<main class="sheet">

  <section class="card card--front" aria-label="Business card front">
    <div class="card__pattern" role="img" aria-label="Dark hexagonal mesh pattern"></div>
    <div class="front__logo">
      <span class="logo__name">7QX</span>
      <span class="logo__mark"></span>
    </div>
    <div class="front__band">Commercial Ceilings, Partitions, Plastering and Carpentry</div>
  </section>

  <section class="card card--back" aria-label="Business card back">
    <div class="card__pattern" role="img" aria-label="Dark hexagonal mesh pattern"></div>
    <div class="back__panel"></div>
    <div class="back__logo">
      <span class="logo__name">7QX Commercial Interiors</span>
      <span class="logo__mark"></span>
    </div>
    <div class="contact">
      <p class="contact__name">Your Name</p>
      <p class="contact__position">Position</p>
      <p class="contact__line">Phone:</p>
      <p class="contact__line">Fax:</p>
      <p class="contact__line">Email:</p>
      <p class="contact__line">Postal Address</p>
    </div>
    <div class="back__band">Web address</div>
  </section>

</main>
</body>
</html>
```